Simple 4 pages Brochure to be modified from existing design.

We're a small Quorvane Apps reseller and need to create brochure for an event urgently. This should be a quick project as you only need to work on the first page mainly.

This is a 4 pages design. A3 fold into A4.

1st Page - Please follow the file "First Page" and "Instruction" to work on this page.

2nd Page - Already provided in PDF. You should be able to edit it in Illustrator. Only need to update 2 lines of text and add in our logo.

3rd Page - Only need to add in our logo in the provided PDF

4th Page - This page should be plain simple with a short description and contact details.

Please visit this page for details:
https://pages.quorvane.example/document/d/7KtWpR3mXq9LzV2nBc8YhJd4FsGe1UoA6iTyNbQ0MwZx/edit?usp=sharing

Please download all the material from here:
https://vault.quorvane.example/file/d/4XpLmRtQwNv8KzYb3HsJcDfGaU7e/edit?usp=sharing

```html
<!DOCTYPE html>
<html lang="en">
<head>
<meta charset="utf-8">
<title>Nexlane – Quorvane Apps for Business Brochure</title>
<link rel="stylesheet" href="https://fonts.googleapis.com/css2?family=Open+Sans:wght@400;600;700;800&display=swap">
<style>
  :root {
    --canvas: #e4e4e4;
    --paper: #ffffff;
    --ink: #111111;
    --body-ink: #5a5a5a;
    --logo-grey: #8a8a8a;
    --muted: #9a9a9a;
    --icon-blue: #3b7ddd;
    --icon-red: #d9443a;
    --icon-yellow: #f2b51e;
    --icon-green: #2f9e55;
    --badge-fill: #d6dde8;
    --badge-edge: #b9c4d4;
  }
  * { box-sizing: border-box; margin: 0; padding: 0; }
  html, body { width: 1200px; height: 1000px; overflow: hidden; }
  body {
    background: var(--canvas);
    font-family: "Open Sans", Arial, sans-serif;
    position: relative;
  }
  .page {
    position: absolute;
    top: 146px;
    width: 500px;
    height: 707px;
    background: var(--paper);
    box-shadow: 0 6px 22px rgba(0,0,0,0.18);
  }
  .page--front { left: 70px; }
  .page--back { left: 630px; }

  /* Front page */
  .brand-mark {
    position: absolute;
    left: 32px;
    top: 48px;
    font-size: 17px;
    font-weight: 600;
    color: var(--body-ink);
    letter-spacing: 0.2px;
  }
  .intro {
    position: absolute;
    left: 168px;
    top: 44px;
    width: 300px;
    color: var(--body-ink);
    font-size: 6.6px;
    line-height: 1.5;
  }
  .intro__title {
    font-size: 13px;
    font-weight: 700;
    color: var(--ink);
    line-height: 1.25;
    margin-bottom: 8px;
  }
  .intro p { margin-bottom: 6px; }
  .benefits { list-style: none; margin-bottom: 6px; }
  .benefits li {
    display: flex;
    align-items: center;
    gap: 6px;
    margin-bottom: 2px;
  }
  .benefits__icon { width: 9px; height: 9px; flex: none; }

  .front-footer {
    position: absolute;
    left: 32px;
    right: 32px;
    bottom: 40px;
    height: 80px;
  }
  .company-name {
    font-weight: 800;
    color: var(--logo-grey);
    letter-spacing: -0.5px;
  }
  .front-footer .company-name {
    position: absolute;
    left: 0;
    bottom: 4px;
    font-size: 30px;
  }
  .front-footer .tagline {
    position: absolute;
    left: 140px;
    bottom: 12px;
    font-size: 10.5px;
    font-weight: 700;
    color: var(--ink);
    line-height: 1.15;
  }
  .front-footer .web {
    position: absolute;
    right: 0;
    top: 0;
    font-size: 9px;
    font-weight: 700;
    color: var(--ink);
  }

  /* Back page */
  .back-brand {
    position: absolute;
    left: 0;
    right: 0;
    top: 240px;
    text-align: center;
    font-size: 44px;
  }
  .badges {
    position: absolute;
    left: 0;
    right: 0;
    top: 372px;
    display: flex;
    justify-content: center;
    gap: 14px;
  }
  .badge {
    width: 34px;
    height: 26px;
    background: var(--badge-fill);
    border: 1px solid var(--badge-edge);
  }
  .back-tagline {
    position: absolute;
    left: 0; right: 0;
    top: 420px;
    text-align: center;
    font-size: 11px;
    color: var(--muted);
    line-height: 1.2;
  }
  .back-web {
    position: absolute;
    left: 0; right: 0;
    top: 478px;
    text-align: center;
    font-size: 13px;
    color: var(--muted);
  }
</style>
</head>
<body>

<section class="page page--front">
  <div class="brand-mark">Quorvane</div>

  <div class="intro">
    <h1 class="intro__title">Welcome to a new way of working:<br>Quorvane Apps for Business.</h1>
    <p>Over four million businesses worldwide already use Quorvane Apps, with thousands more signing up each day. Businesses are moving to the cloud for lots of reasons – improved teamwork, increased productivity, enhanced mobility, impressive ROI, and much more.</p>
    <p>Here are just a few of the major benefits your business will gain by moving to the cloud with Quorvane Apps for Business:</p>
    <ul class="benefits">
      <li><svg class="benefits__icon" viewBox="0 0 10 10"><circle cx="5" cy="5" r="5" fill="var(--icon-blue)"/></svg>Pure and proven cloud – flexibility and security</li>
      <li><svg class="benefits__icon" viewBox="0 0 10 10"><circle cx="5" cy="5" r="5" fill="var(--icon-red)"/></svg>Designed for teams – ideal for dispersed workers</li>
      <li><svg class="benefits__icon" viewBox="0 0 10 10"><circle cx="5" cy="5" r="5" fill="var(--icon-yellow)"/></svg>Productive anywhere – from email, search, and mobile</li>
      <li><svg class="benefits__icon" viewBox="0 0 10 10"><circle cx="5" cy="5" r="5" fill="var(--icon-green)"/></svg>Simple and affordable – people intuitively know how to use it</li>
    </ul>
    <p>Companies of every size, in every industry, and in every part of the world, are using Quorvane Apps to save time, reduce costs, and improve how employees securely collaborate and innovate together.</p>
    <p>With Quorvane Apps, we strive to simplify desktop and smartphone and tablet computing. Whether that means eliminating the expense of locally installed software or logging onto a laptop for all cloud computing, we want to help you do away with high cost seat licenses and desktop software management hassles.</p>
    <p>Say goodbye to frequent software updates and security patches, version and device barriers, choppy teamwork and high-cost licenses. Say hello to Quorvane Apps for Business. The new way of working. Now.</p>
    <p>We know that making a switch like this takes research, and we wouldn't expect you to make the decision to go Quorvane without weighing the pros and cons of our product against those of our competitors. Take your time to study the landscape – we'll be right here when you're ready to make the move.</p>
  </div>

  <footer class="front-footer">
    <div class="company-name">Nexlane</div>
    <div class="tagline">your data your data your data<br>your data your data<br>your data</div>
    <div class="web">www.website.com</div>
  </footer>
</section>

<section class="page page--back">
  <div class="back-brand company-name">Nexlane</div>
  <div class="badges">
    <div class="badge"></div>
    <div class="badge"></div>
    <div class="badge"></div>
  </div>
  <div class="back-tagline">your data your data your data<br>your data your data<br>your data</div>
  <div class="back-web">www.website.com</div>
</section>

</body>
</html>
```